Real Estate Website

The existing website design is http://brenlowa.quillet7.com.au/ and we are not happy with it and need a fresh new design.

The menu of the website should be as it is however the content on the home page needs to include the following:

* Some sort of feature image/slideshow
* Introduction text and photo
* Our services section with boxes for 'strata management' 'property management' and 'property valuation & brokerage'. These boxes will then link to specific areas in the website
* Where are we with the contact details
* contact us with a form asking for name, email, phone, service interested in (as a dropdown) and comments box.
(do not include the who we are section)

In regards to design style/layout, here is what we like:
https://duvernabeans.com/us/
https://www.coverkin.com.au/
https://www.pembrake.com.au/
https://www.lqt.com/
https://www.vorlund.com.au/

```html
<!DOCTYPE html>
<html lang="en">
<head>
<meta charset="utf-8">
<title>Brenlowa &amp; Quill — Real Estate</title>
<link rel="stylesheet" href="https://fonts.googleapis.com/css2?family=Lora:wght@400;500;600;700&display=swap">
<style>
:root{
  --navy:#272a84;
  --navy-deep:#1d206a;
  --lilac:#efeff8;
  --text:#6b6b74;
  --ink:#1f1f24;
  --white:#ffffff;
  --faint:#eaeaec;
}
*{box-sizing:border-box;margin:0;padding:0}
html,body{width:1200px;height:3840px;overflow:hidden}
body{position:relative;font-family:'Lora',Georgia,serif;color:var(--text);background:var(--white)}
.abs{position:absolute}

/* header */
.site-header{left:0;top:0;width:1200px;height:72px;background:var(--navy)}
.brand{left:145px;top:14px;font-size:33px;font-weight:600;color:var(--white);letter-spacing:.2px}
.main-nav{left:528px;top:24px;display:flex;gap:42px;font-size:16px;color:var(--white)}
.main-nav .active{border-bottom:2px solid var(--white);padding-bottom:5px}
.login-btn{left:945px;top:18px;width:110px;height:35px;background:var(--white);color:var(--navy);font-size:13px;font-weight:700;display:flex;align-items:center;justify-content:center}

/* hero */
.hero{left:0;top:72px;width:1200px;height:610px;background:linear-gradient(180deg,#5d7391 0%,#3c4a5e 45%,#2f3a2e 80%,#47603a 100%)}
.hero-title{left:0;top:235px;width:1200px;text-align:center;font-size:104px;font-weight:600;color:var(--white);text-shadow:0 4px 10px rgba(0,0,0,.35)}
.hero-sub{left:0;top:383px;width:1200px;text-align:center;font-size:26px;font-weight:500;color:var(--white);text-shadow:0 2px 6px rgba(0,0,0,.4)}
.hero-btn{left:495px;top:452px;width:210px;height:51px;background:var(--navy);color:var(--white);font-size:17px;font-weight:700;display:flex;align-items:center;justify-content:center;gap:10px}
.arrow{width:38px;height:38px;border-radius:50%;background:#16181f;display:flex;align-items:center;justify-content:center}
.dots{left:564px;top:612px;display:flex;gap:6px}
.dots span{width:10px;height:10px;border-radius:50%;background:var(--white)}
.dots span.on{background:transparent;border:2px solid var(--white)}

/* welcome */
.welcome-band{left:0;top:682px;width:1200px;height:533px;background:var(--lilac)}
.welcome-deco{left:1070px;top:690px;font-size:120px;font-weight:700;color:#dcdff0;writing-mode:vertical-rl;transform:rotate(180deg);line-height:1}
.section-title{left:0;width:1200px;text-align:center;font-size:50px;font-weight:600;color:var(--ink)}
.section-title em{font-style:normal;color:var(--navy)}
.welcome-text{left:240px;top:866px;width:720px;text-align:center;font-size:14.5px;line-height:27px}
.video{left:248px;top:1004px;width:705px;height:407px;background:linear-gradient(135deg,#9fb3cf 0%,#7d8fb6 45%,#5b6ea5 100%)}
.play{left:569px;top:1176px}

/* services */
.services-deco{left:0;top:1480px;width:1200px;text-align:center;font-size:115px;font-weight:700;color:var(--faint);letter-spacing:2px}
.service-img{width:418px;height:373px}
.service-title{font-size:29px;font-weight:600;color:var(--ink)}
.service-text{width:450px;font-size:14.5px;line-height:27px}
.read-btn{width:137px;height:40px;background:var(--navy);color:var(--white);font-size:12px;font-weight:700;display:flex;align-items:center;justify-content:center;gap:8px}

/* contact */
.contact-band{left:0;top:3143px;width:1200px;height:607px;background:linear-gradient(160deg,#2c2f8f 0%,var(--navy) 50%,#23267a 100%)}
.contact-deco{left:0;top:3195px;width:1200px;text-align:center;font-size:120px;font-weight:700;color:rgba(255,255,255,.07)}
.contact-title{left:0;top:3258px;width:1200px;text-align:center;font-size:48px;font-weight:600;color:var(--white)}
.field{background:var(--white);font-size:11px;color:#333;padding:0 20px;display:flex;align-items:center;justify-content:space-between}
.field.area{align-items:flex-start;padding-top:14px}
.submit{left:190px;top:3633px;width:136px;height:39px;background:#14163a;color:var(--white);font-size:12px;font-weight:700;display:flex;align-items:center;justify-content:center;gap:8px}
.info-icon{width:40px;height:40px;border-radius:50%;border:2px solid var(--white);display:flex;align-items:center;justify-content:center}
.info-text{left:815px;font-size:13px;line-height:21px;color:var(--white)}

/* footer */
.copyright{left:143px;top:3788px;font-size:13px;color:#333}
.social{width:36px;height:36px;border-radius:50%;border:2px solid var(--navy)}
</style>
</head>
<body>

<header class="abs site-header">
  <div class="abs brand">Brenlowa &amp; Quill</div>
  <nav class="abs main-nav"><span class="active">Home</span><span>About Us</span><span>Services</span><span>Contact Us</span></nav>
  <div class="abs login-btn">CLIENT LOGIN</div>
</header>

<section class="abs hero" role="img" aria-label="Modern glass office building beside trees and lawn at sunset"></section>
<h1 class="abs hero-title">Brenlowa &amp; Quill</h1>
<p class="abs hero-sub">With 130 Years behind us, we have a lot to offer</p>
<div class="abs hero-btn">GET STARTED
  <svg width="15" height="15" viewBox="0 0 16 16"><circle cx="8" cy="8" r="8" fill="#fff"/><path d="M6.5 4.5 10 8l-3.5 3.5" stroke="#272a84" stroke-width="2" fill="none"/></svg>
</div>
<div class="abs arrow" style="left:66px;top:328px"><svg width="12" height="12" viewBox="0 0 12 12"><path d="M8 2 4 6l4 4" stroke="#fff" stroke-width="2" fill="none"/></svg></div>
<div class="abs arrow" style="left:1096px;top:328px"><svg width="12" height="12" viewBox="0 0 12 12"><path d="M4 2l4 4-4 4" stroke="#fff" stroke-width="2" fill="none"/></svg></div>
<div class="abs dots"><span></span><span></span><span class="on"></span><span></span><span></span></div>

<section class="abs welcome-band"></section>
<div class="abs welcome-deco">WELCOME</div>
<h2 class="abs section-title" style="top:770px">Welcome to <em>Brenlowa &amp; Quill</em></h2>
<p class="abs welcome-text">Brenlowa &amp; Quill was formed in 1888 by the then 20 year old J W Brenlowa, later to become Mayor of Waverley. The company grew on the strength of its management department and the successful Auction of residential subdivisions in the developing suburbs of Waverley, Coogee, Randwick and Clovelly.</p>
<div class="abs video" role="img" aria-label="Business people shaking hands across a desk in a bright office"></div>
<svg class="abs play" width="62" height="62" viewBox="0 0 62 62"><circle cx="31" cy="31" r="28" fill="rgba(255,255,255,.15)" stroke="#fff" stroke-width="4"/><path d="M25 19v24l19-12z" fill="#fff"/></svg>

<div class="abs services-deco">OUR SERVICES</div>
<h2 class="abs section-title" style="top:1540px">Our <em>Services</em></h2>

<div class="abs service-img" style="left:143px;top:1688px;background:linear-gradient(135deg,#e6e4df,#b8b1a6 60%,#8d7a66)" role="img" aria-label="Two colleagues reviewing plans at a desk"></div>
<h3 class="abs service-title" style="left:604px;top:1712px">Strata Management</h3>
<p class="abs service-text" style="left:604px;top:1768px">Brenlowa &amp; Quill has specialised in Strata Management since the introduction of the original Strata Titles Act in 1961. David Quill was issued with one of the first Strata Managers licenses in New South Wales and the office is now headed and run by his son, Oliver.<br>We have developed various different levels of management to suit the requirement of owner's corporations. We can tailor our service to meet your individual needs.</p>
<div class="abs read-btn" style="left:605px;top:1989px">READ MORE <svg width="12" height="12" viewBox="0 0 16 16"><circle cx="8" cy="8" r="8" fill="#fff"/><path d="M6.5 4.5 10 8l-3.5 3.5" stroke="#272a84" stroke-width="2" fill="none"/></svg></div>

<h3 class="abs service-title" style="left:143px;top:2200px">Property Management</h3>
<p class="abs service-text" style="left:143px;top:2256px;width:460px">Our Property Management department has been the backbone of the company for over 100 years.We provide expert advice and service at competitive rates in relation to properties managed by us. Our portfolio includes properties from studio apartments through to retail and commercial properties.Many of our rental clients own units in the Strata buildings we manage which enables us too quickly and efficiently deal with any repair matters</p>
<div class="abs read-btn" style="left:143px;top:2476px">READ MORE <svg width="12" height="12" viewBox="0 0 16 16"><circle cx="8" cy="8" r="8" fill="#fff"/><path d="M6.5 4.5 10 8l-3.5 3.5" stroke="#272a84" stroke-width="2" fill="none"/></svg></div>
<div class="abs service-img" style="left:635px;top:2176px;background:linear-gradient(135deg,#efece6,#d8c8ae 55%,#b08a5e)" role="img" aria-label="Couple unpacking moving boxes in a new kitchen"></div>

<div class="abs service-img" style="left:143px;top:2663px;background:linear-gradient(135deg,#d7dde2,#8e969c 55%,#3b3f44)" role="img" aria-label="Team meeting around a boardroom table"></div>
<h3 class="abs service-title" style="left:604px;top:2688px">Property Valuation &amp; Brokerage</h3>
<p class="abs service-text" style="left:604px;top:2744px;width:455px">In 2011, Brenlowa &amp; Quill (Valuers) merged with Tamsett Valuers to form BQ Valuers.Drawing on more than 20 years experience in all facets of property valuation, BQ Valuers specialise in Strata insurance and replacement assessments. This service ensures that Owners Corporations meet their obligations with regard to adequate insurance cover for their buildings. For more information on our services please click on our services page.</p>
<div class="abs read-btn" style="left:605px;top:2965px">READ MORE <svg width="12" height="12" viewBox="0 0 16 16"><circle cx="8" cy="8" r="8" fill="#fff"/><path d="M6.5 4.5 10 8l-3.5 3.5" stroke="#272a84" stroke-width="2" fill="none"/></svg></div>

<section class="abs contact-band" role="img" aria-label="Apartment buildings in deep blue tint"></section>
<div class="abs contact-deco">CONTACT</div>
<h2 class="abs contact-title">Request a quote</h2>

<div class="abs field" style="left:190px;top:3402px;width:244px;height:42px">Enter Name</div>
<div class="abs field" style="left:443px;top:3402px;width:245px;height:42px">Enter Email</div>
<div class="abs field" style="left:190px;top:3455px;width:244px;height:42px">Enter Phone</div>
<div class="abs field" style="left:443px;top:3455px;width:245px;height:42px">Service interested in
  <svg width="10" height="8" viewBox="0 0 10 8"><path d="M1 2l4 4 4-4" stroke="#222" stroke-width="2" fill="none"/></svg></div>
<div class="abs field area" style="left:190px;top:3508px;width:498px;height:90px">Comments</div>
<div class="abs submit">SUBMIT <svg width="12" height="12" viewBox="0 0 16 16"><circle cx="8" cy="8" r="8" fill="#fff"/><path d="M6.5 4.5 10 8l-3.5 3.5" stroke="#14163a" stroke-width="2" fill="none"/></svg></div>

<div class="abs info-icon" style="left:758px;top:3403px"><svg width="16" height="18" viewBox="0 0 16 20"><path d="M8 1a6 6 0 0 0-6 6c0 5 6 12 6 12s6-7 6-12a6 6 0 0 0-6-6z" fill="none" stroke="#fff" stroke-width="2"/><circle cx="8" cy="7" r="2" fill="#fff"/></svg></div>
<div class="abs info-text" style="top:3402px">18 Larkfield Road, Randwick<br>New South Wales 2031, Australia</div>

<div class="abs info-icon" style="left:758px;top:3468px"><svg width="16" height="16" viewBox="0 0 16 16"><path d="M3 1l3 3-2 2c1 2 3 4 5 5l2-2 3 3-2 3C7 15 1 9 1 3z" fill="#fff"/></svg></div>
<div class="abs info-text" style="top:3478px">Phone : (02) 9000 4172</div>

<div class="abs info-icon" style="left:758px;top:3518px"><svg width="16" height="16" viewBox="0 0 16 16"><circle cx="8" cy="8" r="7" fill="none" stroke="#fff" stroke-width="2"/><path d="M1 8h14M8 1c3 3 3 11 0 14M8 1c-3 3-3 11 0 14" stroke="#fff" stroke-width="1.3" fill="none"/></svg></div>
<div class="abs info-text" style="top:3517px">reception@brenlowaquill.com.au<br>accounts@brenlowaquill.com.au</div>

<div class="abs info-icon" style="left:758px;top:3578px"><svg width="16" height="16" viewBox="0 0 16 16"><circle cx="8" cy="8" r="7" fill="none" stroke="#fff" stroke-width="2"/><path d="M8 4v4l-3 2" stroke="#fff" stroke-width="2" fill="none"/></svg></div>
<div class="abs info-text" style="top:3576px">Mon - Fri 9:00 am - 5:00 pm<br>Sat - 10:00 am - 04:00 pm<br>Sun - Closed</div>

<footer>
  <p class="abs copyright">© 2021 Brenlowa &amp; Quill.All Rights Reserved &nbsp;| &nbsp;Privacy Policy &nbsp;| &nbsp;Terms and Use</p>
  <div class="abs social" style="left:929px;top:3779px" aria-label="Social link"></div>
  <div class="abs social" style="left:973px;top:3779px" aria-label="Social link"></div>
  <div class="abs social" style="left:1017px;top:3779px" aria-label="Social link"></div>
</footer>

</body>
</html>
```